Luxury Wine Label for New Startup Winery

We need a wine label for our new winery startup. We have worked with a local designer but do not feel the resulting label / logo have the elevation required to present our brand as a luxury wine. Our winery is called "Halvorsen Cellars" and we are focused on extremely high quality hand crafted artisan and estate wines from the Pacific Northwest.
We would like to see designs that utilize a tree line, or other imagery that represents the "Halvorsen" part of our company name. Another interesting feature could be wood grain.
A logo will be required based on your design so please design with this in mind:
This logo should be consistent with the wine bottle label design, and should be representative of our high end exclusive wine while giving a sense of place (Oregon/ Pacific Northwest.)
I will supply an image of the design we received from our local designer, PLEASE NOTE: in general we do like wood grain and tree line concepts but feel the execution was poorly done.
ATTN: Logo design should be suitable for use on: Bottles (Red wine/rose/white wine), Bussiness cards, vehicle signage, business signage, etc
P.S.:
If you have a design that is not outside the box we are still interested in seeing it.
Label is for a burgundy style bottle with a label height of 3.5 - 4" and a width of 3.5-4"
any label <= 4"x4" and >=3.5"x3.5" will be acceptable:
HOWEVER Width should be greater than or equal to height due to the bottle format
Target Market(s)
Wine enthusiasts with adequate discretionary budgets to afford $100 bottles of wine.
Industry/Entity Type
Wine / Winery
Requirements
Must have
- A sense of luxury, a feel of exclusivity, and a theme consistent with our product and brand name
Nice to have
- Tree line, wood grain or other wood themes. Serif fonts
Should not have
- anything cheesy, off topic, hard to read script fonts or anything that makes the label hard to read from a few feet away or too busy

```html
<!DOCTYPE html>
<html lang="en">
<head>
<meta charset="utf-8">
<title>Halvorsen Cellars – Syrah Label</title>
<link href="https://fonts.googleapis.com/css2?family=Cinzel:wght@400&display=swap" rel="stylesheet">
<style>
  :root {
    --page: #ffffff;
    --label-black: #000000;
    --rule-grey: #333333;
    --ivory: #f6f1e8;
    --wood-dark: #5b2f17;
    --wood-mid: #7b4424;
    --wood-light: #92592f;
    --gold: #d9a420;
    --gold-deep: #a8661a;
    --gold-bright: #f1cf45;
  }
  * { box-sizing: border-box; margin: 0; padding: 0; }
  html, body {
    width: 1200px;
    height: 848px;
    overflow: hidden;
    background: var(--page);
  }
  .canvas {
    position: relative;
    width: 1200px;
    height: 848px;
  }
  .label {
    position: absolute;
    left: 74px;
    top: 199px;
    width: 416px;
  }
  .label-main {
    position: relative;
    height: 337px;
    background: var(--label-black);
  }
  .rule {
    position: absolute;
    left: 24px;
    right: 28px;
    height: 1px;
    background: var(--rule-grey);
  }
  .rule--top { top: 27px; }
  .rule--bottom { bottom: 26px; }
  .treeline-art {
    position: absolute;
    left: 134px;
    top: 49px;
    width: 137px;
    height: 75px;
    background:
      radial-gradient(ellipse at 70% 85%, var(--gold-bright) 0%, rgba(241,207,69,0) 60%),
      linear-gradient(100deg, var(--gold-deep) 0%, var(--gold) 50%, var(--gold-bright) 100%);
    opacity: 0.9;
  }
  .brand-name,
  .brand-sub {
    position: absolute;
    left: 0;
    right: 0;
    text-align: center;
    font-family: "Cinzel", serif;
    font-weight: 400;
    color: var(--ivory);
    line-height: 1;
  }
  .brand-name {
    top: 137px;
    font-size: 39px;
    letter-spacing: 0.02em;
  }
  .brand-sub {
    top: 178px;
    font-size: 15px;
    letter-spacing: 0.6em;
    padding-left: 0.6em;
  }
  .varietal-band {
    position: relative;
    height: 90px;
    margin-top: 14px;
    background:
      linear-gradient(90deg, rgba(60,28,10,0.35) 0%, rgba(60,28,10,0) 30%, rgba(150,95,55,0.18) 55%, rgba(60,28,10,0.3) 100%),
      linear-gradient(180deg, var(--wood-light) 0%, var(--wood-mid) 50%, var(--wood-dark) 100%);
    text-align: center;
    font-family: "Cinzel", serif;
    color: var(--ivory);
    line-height: 1;
  }
  .region {
    position: absolute;
    left: 0; right: 0; top: 21px;
    font-size: 15px;
    letter-spacing: 0.02em;
  }
  .varietal {
    position: absolute;
    left: 0; right: 0; top: 40px;
    font-size: 21px;
    letter-spacing: 0.04em;
  }
  .vintage-line {
    position: absolute;
    left: 0; right: 0; top: 64px;
    font-size: 9px;
    letter-spacing: 0.4em;
    padding-left: 0.4em;
  }
  .gold-rule {
    position: absolute;
    height: 1px;
    background: var(--gold);
  }
  .gold-rule--top {
    left: 150px;
    right: 20px;
    top: 12px;
    opacity: 0.45;
  }
  .gold-rule--bottom {
    left: 12px;
    right: 13px;
    top: 77px;
  }
</style>
</head>
<body>
  <main class="canvas">
    <article class="label">
      <section class="label-main">
        <div class="rule rule--top"></div>
        <div class="treeline-art" role="img" aria-label="Gold foil tree line over a rolling hillside"></div>
        <h1 class="brand-name">HALVORSEN</h1>
        <p class="brand-sub">CELLARS</p>
        <div class="rule rule--bottom"></div>
      </section>
      <section class="varietal-band" role="img" aria-label="Dark walnut wood grain band">
        <div class="gold-rule gold-rule--top"></div>
        <p class="region">WILLAMETTE VALLEY</p>
        <p class="varietal">SYRAH</p>
        <p class="vintage-line">ESTATE | 2023 | GROWN</p>
        <div class="gold-rule gold-rule--bottom"></div>
      </section>
    </article>
  </main>
</body>
</html>
```